Swiss Consultant for Enterprises and SME's is in Need for PPT for Teaching/Presenting

I am looking for a powerpointpresentation template (must be with slidemaster) for presenting my company and also for teaching. Colors must be taken from Logo and content can be taken from website if needed.

It is either used to present anything regarding finances and ERP-Systemrelated topics (espeically Kortel Ledger Pro) and also teach anything regarding Finance and or ERP-Systems in an industrial or financial environment.

Low design quality

Font styles to use
Sans Serif

Requirements
Must have
• I need at least following slides (Title, Subtitle/Section, Index, Single content, Empty (just logo), two content, tree content -> each as column and at last 4 / 5 & 6 infographics (done with o365 "standard" Icons)
• Coloring white and same as logo provided no additional colors except for charts etc.(matching to logostyle)
• Also I need a Word template such as the one attached.
Nice to have
• any additional infographic
Should not have
• Presentation must be done in the slidemaster as a template anything else will not be accepted.
• Letterhead is not needed I only need a Document for Documentation.

```html
<!DOCTYPE html>
<html lang="en">
<head>
<meta charset="utf-8">
<title>Brightal Consulting – Presentation Template Overview</title>
<link href="https://fonts.googleapis.com/css2?family=Open+Sans:wght@400;600;700&display=swap" rel="stylesheet">
<style>
:root{
  --blue:#3a72b8;
  --blue-dark:#2a5a98;
  --blue-soft:#5b8ccb;
  --grey:#6e6e6e;
  --grey-dark:#4a4a4a;
  --board:#b9b9b9;
  --ink:#333;
  --muted:#8a8a8a;
  --white:#fff;
}
*{margin:0;padding:0;box-sizing:border-box}
html,body{width:1184px;height:1200px;overflow:hidden}
body{background:var(--board);font-family:"Open Sans",Arial,sans-serif;position:relative}
.slide{position:absolute;width:239px;height:134px;background:var(--white);overflow:hidden;box-shadow:0 1px 2px rgba(0,0,0,.18)}
.abs{position:absolute}
.hd{position:absolute;left:9px;top:7px;font-size:4.4px;font-weight:700;color:var(--ink);letter-spacing:.1px}
.hd::after{content:"";display:block;width:12px;height:.8px;background:var(--blue);margin-top:1.4px}
.photo{position:absolute;background:linear-gradient(135deg,#8fa6bf,#5d7a9c 55%,#3f5b7d)}
.photo.warm{background:linear-gradient(135deg,#c9b39e,#8d7765 55%,#5a4c44)}
.photo.grey{background:linear-gradient(135deg,#d4d4d4,#8e8e8e 60%,#5c5c5c)}
.photo.blue{background:linear-gradient(135deg,#5d8fcf,#2f63a6)}
.tx{font-size:2.5px;line-height:3.3px;color:var(--muted)}
.tx.w{color:#eaf1fb}
.tx.c{text-align:center}
.lbl{font-size:3.2px;font-weight:700;color:var(--blue);text-align:center}
.lbl.l{text-align:left}
.lbl.r{text-align:right}
.icon-cell{display:flex;flex-direction:column;align-items:center;height:45px}
.icon-cell svg{width:10px;height:10px;margin-bottom:2px}
.icon-cell .lbl{color:var(--ink);margin-bottom:1px}
.row-stack{position:absolute;display:flex;flex-direction:column}
.row-stack > div{height:24px;padding-top:2px}
.row-stack.tight > div{height:23px}
</style>
</head>
<body>

<!-- Row 1 -->
<section class="slide title-slide" style="left:78px;top:77px">
  <div class="photo blue" style="left:0;top:0;width:239px;height:108px" role="img" aria-label="Business team meeting photo with blue overlay"></div>
  <h1 class="abs" style="left:19px;top:44px;color:#fff;font-size:11.5px;line-height:14px;font-weight:600">Edit title and<br>description here</h1>
  <div class="abs" style="left:13px;top:116px;font-size:8px;font-weight:700;color:var(--blue-dark)">Brightal</div>
  <div class="abs" style="right:12px;top:119px;font-size:3.6px;font-weight:700;color:var(--blue)">www.brightalconsulting.com</div>
</section>

<section class="slide intro-slide" style="left:340px;top:77px">
  <div class="hd">EDIT TITLE HERE</div>
  <div class="abs" style="left:21px;top:30px;width:76px;height:89px;background:var(--blue);padding:9px 6px">
    <p class="tx w">Lorem ipsum dolor sit amet, consectetur adipiscing elit, sed do eiusmod tempor incididunt ut labore.</p>
    <p class="tx w" style="margin-top:3px">Lorem ipsum dolor sit amet, consectetur adipiscing elit, sed do eiusmod tempor incididunt ut labore.</p>
  </div>
  <div class="photo warm" style="left:97px;top:30px;width:135px;height:89px" role="img" aria-label="Consultants working at a laptop"></div>
</section>

<section class="slide team-slide" style="left:598px;top:77px">
  <div class="hd">EDIT TITLE HERE</div>
  <div class="photo grey" style="left:27px;top:37px;width:33px;height:33px;border-radius:50%" role="img" aria-label="Portrait of team member"></div>
  <div class="photo grey" style="left:78px;top:37px;width:33px;height:33px;border-radius:50%" role="img" aria-label="Portrait of team member"></div>
  <div class="photo warm" style="left:128px;top:37px;width:33px;height:33px;border-radius:50%" role="img" aria-label="Portrait of team member"></div>
  <div class="photo grey" style="left:179px;top:37px;width:33px;height:33px;border-radius:50%" role="img" aria-label="Portrait of team member"></div>
  <div class="abs lbl" style="left:18px;top:75px;width:51px">CLARA VENN<div class="tx">General Manager</div></div>
  <div class="abs lbl" style="left:69px;top:75px;width:51px">MARCO FEHR<div class="tx">Trainee Head</div></div>
  <div class="abs lbl" style="left:119px;top:75px;width:51px">LUCA BRANDT<div class="tx">Finance</div></div>
  <div class="abs lbl" style="left:170px;top:75px;width:51px">TOBIAS KELLER<div class="tx">Senior Trainer</div></div>
  <p class="abs tx c" style="left:20px;top:92px;width:199px">Lorem ipsum dolor sit amet, consectetur adipiscing elit, sed do eiusmod tempor incididunt ut labore. Lorem ipsum dolor sit amet, consectetur adipiscing elit, sed do eiusmod tempor incididunt ut labore. Lorem ipsum dolor sit amet, consectetur adipiscing elit, sed do eiusmod tempor incididunt ut labore.</p>
</section>

<section class="slide three-photo-slide" style="left:856px;top:77px">
  <div class="hd">EDIT TITLE HERE</div>
  <div class="photo" style="left:11px;top:22px;width:70px;height:57px;border-bottom:2px solid var(--blue)" role="img" aria-label="Woman in a server room"></div>
  <div class="photo warm" style="left:84px;top:22px;width:70px;height:57px;border-bottom:2px solid var(--blue)" role="img" aria-label="Colleagues smiling in the office"></div>
  <div class="photo" style="left:157px;top:22px;width:70px;height:57px;border-bottom:2px solid var(--blue)" role="img" aria-label="Colour swatches on a desk"></div>
  <div class="abs lbl" style="left:11px;top:93px;width:70px">LOREM IPSUM<p class="tx c" style="margin-top:2px">Lorem ipsum dolor sit amet, consectetur adipiscing elit, sed do eiusmod tempor incididunt ut labore.</p></div>
  <div class="abs lbl" style="left:84px;top:93px;width:70px">LOREM IPSUM<p class="tx c" style="margin-top:2px">Lorem ipsum dolor sit amet, consectetur adipiscing elit, sed do eiusmod tempor incididunt ut labore.</p></div>
  <div class="abs lbl" style="left:157px;top:93px;width:70px">LOREM IPSUM<p class="tx c" style="margin-top:2px">Lorem ipsum dolor sit amet, consectetur adipiscing elit, sed do eiusmod tempor incididunt ut labore.</p></div>
</section>

<!-- Row 2 -->
<section class="slide icon-grid-slide" style="left:78px;top:235px">
  <div class="hd">EDIT TITLE HERE</div>
  <div class="abs" style="left:22px;top:31px;width:196px;display:grid;grid-template-columns:repeat(5,1fr);column-gap:5px">
    <div class="icon-cell"><svg viewBox="0 0 10 10" fill="var(--blue)"><path d="M1 8a2 2 0 0 1 1-3.5a3 3 0 0 1 5.5-.5a2 2 0 0 1 1.5 4z"/></svg><div class="lbl">LOREM IPSUM</div><p class="tx c">Lorem ipsum dolor sit amet, consectetur elit sed do.</p></div>
    <div class="icon-cell"><svg viewBox="0 0 10 10"><circle cx="5" cy="5" r="3.8" fill="none" stroke="var(--blue)" stroke-width="1"/></svg><div class="lbl">LOREM IPSUM</div><p class="tx c">Lorem ipsum dolor sit amet, consectetur elit sed do.</p></div>
    <div class="icon-cell"><svg viewBox="0 0 10 10" fill="var(--blue)"><path d="M0.5 3l4.5-2.5l4.5 2.5zM1 3.6h8v.8h-8zM1.5 4.8h1v3h-1zM4.5 4.8h1v3h-1zM7.5 4.8h1v3h-1zM0.5 8.2h9v1h-9z"/></svg><div class="lbl">LOREM IPSUM</div><p class="tx c">Lorem ipsum dolor sit amet, consectetur elit sed do.</p></div>
    <div class="icon-cell"><svg viewBox="0 0 10 10" fill="var(--blue)"><circle cx="4" cy="4" r="3"/><circle cx="7" cy="6.5" r="2.5"/></svg><div class="lbl">LOREM IPSUM</div><p class="tx c">Lorem ipsum dolor sit amet, consectetur elit sed do.</p></div>
    <div class="icon-cell"><svg viewBox="0 0 10 10" fill="var(--blue)"><path d="M1 2.5h8v5.5h-8z"/><path d="M1 2.5l4 3l4-3" fill="none" stroke="#fff" stroke-width=".6"/></svg><div class="lbl">LOREM IPSUM</div><p class="tx c">Lorem ipsum dolor sit amet, consectetur elit sed do.</p></div>
    <div class="icon-cell"><svg viewBox="0 0 10 10"><circle cx="5" cy="5" r="3.8" fill="none" stroke="var(--blue)" stroke-width="1"/><path d="M5 3v2.2l1.5 1" stroke="var(--blue)" stroke-width=".8" fill="none"/></svg><div class="lbl">LOREM IPSUM</div><p class="tx c">Lorem ipsum dolor sit amet, consectetur elit sed do.</p></div>
    <div class="icon-cell"><svg viewBox="0 0 10 10" fill="var(--blue)"><circle cx="3.5" cy="3.5" r="2.5"/><circle cx="7" cy="7" r="2"/></svg><div class="lbl">LOREM IPSUM</div><p class="tx c">Lorem ipsum dolor sit amet, consectetur elit sed do.</p></div>
    <div class="icon-cell"><svg viewBox="0 0 10 10" fill="var(--blue)"><path d="M1 3h8v6h-8zM3.5 1.5h3v1.5h-3z"/><circle cx="5" cy="6" r="1.5" fill="#fff"/></svg><div class="lbl">LOREM IPSUM</div><p class="tx c">Lorem ipsum dolor sit amet, consectetur elit sed do.</p></div>
    <div class="icon-cell"><svg viewBox="0 0 10 10"><path d="M1.5 2h7v7h-7z" fill="none" stroke="var(--blue)" stroke-width="1"/><path d="M3 7l4-4" stroke="var(--blue)" stroke-width="1"/></svg><div class="lbl">LOREM IPSUM</div><p class="tx c">Lorem ipsum dolor sit amet, consectetur elit sed do.</p></div>
    <div class="icon-cell"><svg viewBox="0 0 10 10" fill="var(--blue)"><path d="M3.5 0.5h3v4h2.5l-4 4l-4-4h2.5zM0.5 8.8h9v1h-9z"/></svg><div class="lbl">LOREM IPSUM</div><p class="tx c">Lorem ipsum dolor sit amet, consectetur elit sed do.</p></div>
  </div>
</section>

<section class="slide photo-text-slide" style="left:340px;top:235px">
  <div class="hd">EDIT TITLE HERE</div>
  <div class="photo" style="left:10px;top:26px;width:89px;height:96px" role="img" aria-label="Team reviewing charts around a table"></div>
  <p class="abs tx" style="left:112px;top:31px;width:116px">Lorem ipsum dolor sit amet, consectetur adipiscing elit, sed do eiusmod tempor incididunt ut labore. Lorem ipsum dolor sit amet, consectetur adipiscing elit, sed do eiusmod tempor incididunt ut labore. Lorem ipsum dolor sit amet, consectetur adipiscing elit, sed do eiusmod tempor incididunt ut labore.</p>
  <svg class="abs" style="left:112px;top:80px" width="116" height="14" viewBox="0 0 116 14" fill="var(--blue)">
    <path d="M15 2h10v10h-10z" fill="none" stroke="var(--blue)" stroke-width="1"/><path d="M18 9l2-3l2 3z"/>
    <path d="M52 11h2v-3h-2zM55 11h2v-5h-2zM58 11h2v-7h-2zM61 11h2v-9h-2z"/>
    <path d="M93 3h4v9h-4zM98 1h4v11h-4z"/>
  </svg>
  <div class="abs" style="left:112px;top:97px;width:116px;display:flex;gap:6px">
    <p class="tx c" style="flex:1">Lorem ipsum dolor sit amet, consectetur elit.</p>
    <p class="tx c" style="flex:1">Lorem ipsum dolor sit amet, consectetur elit.</p>
    <p class="tx c" style="flex:1">Lorem ipsum dolor sit amet, consectetur elit.</p>
  </div>
</section>

<section class="slide chart-slide" style="left:598px;top:235px">
  <div class="hd">EDIT TITLE HERE</div>
  <p class="abs tx" style="left:11px;top:26px;width:110px">Lorem ipsum dolor sit amet, consectetur adipiscing elit, sed do eiusmod tempor incididunt ut labore. Lorem ipsum dolor sit amet, consectetur adipiscing elit, sed do eiusmod tempor incididunt ut labore. Lorem ipsum dolor sit amet, consectetur adipiscing elit, sed do eiusmod tempor incididunt ut labore. Lorem ipsum dolor sit amet, consectetur adipiscing elit, sed do eiusmod tempor incididunt ut labore. Lorem ipsum dolor sit amet, consectetur adipiscing elit, sed do eiusmod tempor incididunt ut labore. Lorem ipsum dolor sit amet, consectetur adipiscing elit, sed do eiusmod tempor incididunt ut labore.</p>
  <svg class="abs" style="left:128px;top:40px" width="104" height="80" viewBox="0 0 104 80">
    <g stroke="#e3e3e3" stroke-width=".4"><path d="M10 10h90M10 25h90M10 40h90M10 55h90M10 70h90"/></g>
    <g fill="var(--blue)">
      <rect x="18" y="58" width="6" height="12"/><rect x="30" y="46" width="6" height="24"/>
      <rect x="42" y="32" width="6" height="38"/><rect x="54" y="22" width="6" height="48"/>
      <rect x="66" y="36" width="6" height="34"/><rect x="78" y="50" width="6" height="20"/>
    </g>
    <rect x="49" y="11" width="16" height="5" fill="#3ab0e6"/>
    <text x="57" y="14.8" font-size="2.6" fill="#fff" text-anchor="middle" font-family="Open Sans, sans-serif">Lorem</text>
    <path d="M21 56L33 44L45 30L57 20L69 34L81 48" stroke="#9ab" stroke-width=".4" fill="none"/>
  </svg>
</section>

<section class="slide three-box-slide" style="left:856px;top:235px">
  <div class="hd">EDIT TITLE HERE</div>
  <div class="abs" style="left:13px;top:26px;width:60px;height:96px;background:var(--blue);border-bottom:3px solid var(--blue-dark)"></div>
  <div class="abs" style="left:90px;top:26px;width:60px;height:96px;background:var(--grey);border-bottom:3px solid var(--grey-dark)"></div>
  <div class="abs" style="left:167px;top:26px;width:60px;height:96px;background:var(--blue);border-bottom:3px solid var(--blue-dark)"></div>
  <svg class="abs" style="left:0;top:0" width="239" height="134" viewBox="0 0 239 134" fill="#fff">
    <path d="M33 43h20v15h-20zM39 40h8v3h-8z"/>
    <circle cx="114" cy="43" r="3.5"/><circle cx="124" cy="43" r="3.5"/><circle cx="119" cy="47" r="4"/>
    <path d="M111 58a8 6 0 0 1 16 0zM108 55a5 4 0 0 1 8 0zM122 55a5 4 0 0 1 8 0z"/>
    <path d="M185 45l12-5l12 5l-12 5zM191 48v5a6 3 0 0 0 12 0v-5l-6 2.5z"/>
  </svg>
  <p class="abs tx w c" style="left:17px;top:68px;width:52px">Lorem ipsum dolor sit amet, consectetur adipiscing elit, sed do eiusmod tempor incididunt ut labore.</p>
  <p class="abs tx w c" style="left:94px;top:68px;width:52px">Lorem ipsum dolor sit amet, consectetur adipiscing elit, sed do eiusmod tempor incididunt ut labore.</p>
  <p class="abs tx w c" style="left:171px;top:68px;width:52px">Lorem ipsum dolor sit amet, consectetur adipiscing elit, sed do eiusmod tempor incididunt ut labore.</p>
</section>

<!-- Row 3 -->
<section class="slide section-slide" style="left:78px;top:389px">
  <div class="photo blue" style="left:0;top:0;width:239px;height:134px" role="img" aria-label="Office desk scene with blue overlay"></div>
  <svg class="abs" style="left:36px;top:84px" width="22" height="18" viewBox="0 0 22 18" fill="#fff"><path d="M1 5h20v12h-20zM7 1h8v4h-2v-2h-4v2h-2z"/><path d="M1 10h20" stroke="var(--blue)" stroke-width=".8"/></svg>
  <div class="abs" style="left:65px;top:83px;color:#fff;font-size:9px;font-weight:600">Section Title</div>
  <p class="abs tx w" style="left:65px;top:96px;width:90px">Lorem ipsum dolor sit amet, consectetur elit.</p>
</section>

<section class="slide overview-icons-slide" style="left:340px;top:389px">
  <div class="hd">COMPANY OVERVIEW</div>
  <svg class="abs" style="left:0;top:0" width="239" height="134" viewBox="0 0 239 134" fill="var(--blue)">
    <g><circle cx="122" cy="37" r="6"/><circle cx="122" cy="61" r="6"/><circle cx="122" cy="85" r="6"/><circle cx="122" cy="109" r="6"/>
    <circle cx="161" cy="37" r="6"/><circle cx="161" cy="61" r="6"/><circle cx="161" cy="85" r="6"/><circle cx="161" cy="109" r="6"/></g>
    <g fill="#fff"><path d="M119 35h6v4h-6zM119 34l3-2l3 2z"/><circle cx="120.5" cy="60" r="1.5"/><circle cx="123.5" cy="60" r="1.5"/><path d="M119 87l3-5l3 5z"/><path d="M119 107h6v4h-6z"/>
    <circle cx="161" cy="37" r="2.5"/><path d="M158 59h6v4h-6z"/><path d="M158 87l6-4l-2 5z"/><circle cx="161" cy="109" r="2.5"/></g>
  </svg>
  <div class="row-stack" style="left:20px;top:30px;width:94px">
    <div><div class="lbl r">Lorem ipsum dolor</div><p class="tx" style="text-align:right">Lorem ipsum dolor sit amet, consectetur elit.</p></div>
    <div><div class="lbl r">Lorem ipsum dolor</div><p class="tx" style="text-align:right">Lorem ipsum dolor sit amet, consectetur elit.</p></div>
    <div><div class="lbl r">Lorem ipsum dolor</div><p class="tx" style="text-align:right">Lorem ipsum dolor sit amet, consectetur elit.</p></div>
    <div><div class="lbl r">Lorem ipsum dolor</div><p class="tx" style="text-align:right">Lorem ipsum dolor sit amet, consectetur elit.</p></div>
  </div>
  <div class="row-stack" style="left:172px;top:30px;width:58px">
    <div><div class="lbl l">Lorem ipsum dolor</div><p class="tx">Lorem ipsum dolor sit amet, consectetur elit.</p></div>
    <div><div class="lbl l">Lorem ipsum dolor</div><p class="tx">Lorem ipsum dolor sit amet, consectetur elit.</p></div>
    <div><div class="lbl l">Lorem ipsum dolor</div><p class="tx">Lorem ipsum dolor sit amet, consectetur elit.</p></div>
    <div><div class="lbl l">Lorem ipsum dolor</div><p class="tx">Lorem ipsum dolor sit amet, consectetur elit.</p></div>
  </div>
</section>

<section class="slide overview-list-slide" style="left:598px;top:389px">
  <div class="hd">COMPANY OVERVIEW</div>
  <ol class="abs" style="left:18px;top:28px;width:128px;list-style:none;font-size:2.8px;font-weight:600;color:var(--ink)">
    <li style="display:flex;align-items:center;gap:5px;height:14px;border-bottom:.4px solid #ddd"><span style="background:var(--blue);color:#fff;width:6px;height:6px;flex:none;display:grid;place-items:center">1</span>Leading ledger platform with a broad module portfolio</li>
    <li style="display:flex;align-items:center;gap:5px;height:14px;border-bottom:.4px solid #ddd"><span style="background:var(--blue);color:#fff;width:6px;height:6px;flex:none;display:grid;place-items:center">2</span>New tools for mobile finance reporting</li>
    <li style="display:flex;align-items:center;gap:5px;height:14px;border-bottom:.4px solid #ddd"><span style="background:var(--blue);color:#fff;width:6px;height:6px;flex:none;display:grid;place-items:center">3</span>Strong market share in industrial ERP projects</li>
    <li style="display:flex;align-items:center;gap:5px;height:14px;border-bottom:.4px solid #ddd"><span style="background:var(--blue);color:#fff;width:6px;height:6px;flex:none;display:grid;place-items:center">4</span>Fast rollout for small and medium firms</li>
    <li style="display:flex;align-items:center;gap:5px;height:14px;border-bottom:.4px solid #ddd"><span style="background:var(--blue);color:#fff;width:6px;height:6px;flex:none;display:grid;place-items:center">5</span>Industry leading Kortel Ledger Pro training</li>
    <li style="display:flex;align-items:center;gap:5px;height:18px"><span style="background:var(--blue);color:#fff;width:6px;height:6px;flex:none;display:grid;place-items:center">6</span>Track record of solid execution and steady growth</li>
  </ol>
  <div class="photo" style="left:146px;top:26px;width:84px;height:70px" role="img" aria-label="Hands working on a tablet with data graphics"></div>
</section>

<section class="slide chart-text-slide" style="left:856px;top:389px">
  <div class="hd">EDIT TITLE HERE</div>
  <svg class="abs" style="left:12px;top:24px" width="110" height="100" viewBox="0 0 110 100">
    <g stroke="#e6e6e6" stroke-width=".4"><path d="M12 10h90M12 24h90M12 38h90M12 52h90M12 66h90"/></g>
    <g fill="var(--blue)"><rect x="20" y="61" width="6" height="5"/><rect x="34" y="55" width="6" height="11"/><rect x="48" y="49" width="6" height="17"/><rect x="62" y="40" width="6" height="26"/><rect x="76" y="31" width="6" height="35"/></g>
    <g fill="#8fb2df"><rect x="27" y="58" width="5" height="8"/><rect x="41" y="52" width="5" height="14"/><rect x="55" y="45" width="5" height="21"/><rect x="69" y="35" width="5" height="31"/></g>
    <path d="M22 59L37 52L51 45L65 37L79 28L96 17" stroke="#888" stroke-width=".4" fill="none"/>
    <g fill="var(--blue)"><circle cx="9" cy="90" r="3"/><circle cx="30" cy="90" r="3"/><circle cx="51" cy="90" r="3"/><circle cx="72" cy="90" r="3"/><circle cx="93" cy="90" r="3"/></g>
    <g font-size="2.4" fill="#888" font-family="Open Sans, sans-serif"><text x="14" y="91">Lorem</text><text x="35" y="91">Lorem</text><text x="56" y="91">Lorem</text><text x="77" y="91">Lorem</text><text x="98" y="91">Lorem</text></g>
  </svg>
  <p class="abs tx" style="left:135px;top:22px;width:95px">Lorem ipsum dolor sit amet, consectetur adipiscing elit, sed do eiusmod tempor incididunt ut labore. Lorem ipsum dolor sit amet, consectetur adipiscing elit, sed do eiusmod tempor incididunt ut labore. Lorem ipsum dolor sit amet, consectetur adipiscing elit, sed do eiusmod tempor incididunt ut labore. Lorem ipsum dolor sit amet, consectetur adipiscing elit, sed do eiusmod tempor incididunt ut labore. Lorem ipsum dolor sit amet, consectetur adipiscing elit, sed do eiusmod tempor incididunt ut labore.</p>
</section>

<!-- Row 4 -->
<section class="slide banner-slide" style="left:78px;top:546px">
  <div class="hd">EDIT TITLE HERE</div>
  <div class="photo grey" style="left:0;top:25px;width:239px;height:93px" role="img" aria-label="Silhouettes of business people in a meeting room"></div>
  <div class="abs" style="left:22px;top:25px;width:87px;height:93px;background:var(--blue);padding:14px 8px">
    <div style="color:#fff;font-size:5.5px;font-weight:600">LOREM IPSUM</div>
    <p class="tx w" style="margin-top:5px">Lorem ipsum dolor sit amet, consectetur adipiscing elit, sed do eiusmod tempor incididunt ut labore. Lorem ipsum dolor sit amet, consectetur adipiscing elit, sed do eiusmod tempor incididunt ut labore. Lorem ipsum dolor sit amet, consectetur adipiscing elit, sed do eiusmod tempor incididunt ut labore. Lorem ipsum dolor sit amet, consectetur adipiscing elit, sed do eiusmod tempor incididunt ut labore.</p>
  </div>
</section>

<section class="slide six-box-slide" style="left:340px;top:546px">
  <div class="hd">EDIT TITLE HERE</div>
  <svg class="abs" style="left:0;top:0" width="239" height="134" viewBox="0 0 239 134">
    <g fill="none" stroke="var(--blue-soft)" stroke-width=".6">
      <rect x="31" y="29" width="52" height="38"/><rect x="93" y="29" width="52" height="38"/><rect x="155" y="29" width="52" height="38"/>
      <rect x="31" y="79" width="52" height="38"/><rect x="93" y="79" width="52" height="38"/><rect x="155" y="79" width="52" height="38"/>
    </g>
    <g fill="var(--blue)">
      <path d="M51 25h12v10l-6 4l-6-4z"/><path d="M113 25h12v10l-6 4l-6-4z"/><path d="M175 25h12v10l-6 4l-6-4z"/>
      <path d="M51 75h12v10l-6 4l-6-4z"/><path d="M113 75h12v10l-6 4l-6-4z"/><path d="M175 75h12v10l-6 4l-6-4z"/>
    </g>
    <g fill="#fff"><circle cx="57" cy="31" r="2"/><rect x="117" y="28" width="4" height="6"/><rect x="178" y="29" width="6" height="4"/>
    <circle cx="55.5" cy="80" r="1.3"/><circle cx="58.5" cy="80" r="1.3"/><path d="M114 80l5-2l5 2l-5 3z"/><path d="M178 81l3-2l3 2l-3 2z"/></g>
  </svg>
  <p class="abs tx c" style="left:35px;top:44px;width:44px">Lorem ipsum dolor sit amet, consectetur elit.</p>
  <p class="abs tx c" style="left:97px;top:44px;width:44px">Lorem ipsum dolor sit amet, consectetur elit.</p>
  <p class="abs tx c" style="left:159px;top:44px;width:44px">Lorem ipsum dolor sit amet, consectetur elit.</p>
  <p class="abs tx c" style="left:35px;top:94px;width:44px">Lorem ipsum dolor sit amet, consectetur elit.</p>
  <p class="abs tx c" style="left:97px;top:94px;width:44px">Lorem ipsum dolor sit amet, consectetur elit.</p>
  <p class="abs tx c" style="left:159px;top:94px;width:44px">Lorem ipsum dolor sit amet, consectetur elit.</p>
</section>

<section class="slide columns-slide" style="left:598px;top:546px">
  <div class="hd">EDIT TITLE HERE</div>
  <p class="abs tx" style="left:11px;top:30px;width:62px">Lorem ipsum dolor sit amet, consectetur adipiscing elit, sed do eiusmod tempor incididunt ut labore. Lorem ipsum dolor sit amet, consectetur adipiscing elit, sed do eiusmod tempor incididunt ut labore. Lorem ipsum dolor sit amet, consectetur adipiscing elit, sed do eiusmod tempor incididunt ut labore.</p>
  <div class="photo" style="left:150px;top:22px;width:89px;height:100px" role="img" aria-label="Keyboard and office equipment close-up"></div>
  <div class="abs" style="left:78px;top:30px;width:136px;height:90px;background:var(--blue);display:flex;gap:6px;padding:5px">
    <div style="flex:1"><div style="color:#fff;font-size:3.6px;font-weight:700;text-align:center">Lorem ipsum</div><p class="tx w c" style="margin-top:3px">Lorem ipsum dolor sit amet, consectetur adipiscing elit, sed do eiusmod tempor incididunt ut labore. Lorem ipsum dolor sit amet, consectetur adipiscing elit, sed do eiusmod tempor incididunt ut labore.</p></div>
    <div style="flex:1"><div style="color:#fff;font-size:3.6px;font-weight:700;text-align:center">Lorem ipsum</div><p class="tx w c" style="margin-top:3px">Lorem ipsum dolor sit amet, consectetur adipiscing elit, sed do eiusmod tempor incididunt ut labore. Lorem ipsum dolor sit amet, consectetur adipiscing elit, sed do eiusmod tempor incididunt ut labore.</p></div>
  </div>
</section>

<section class="slide timeline-slide" style="left:856px;top:546px">
  <div class="hd">EDIT TITLE HERE</div>
  <svg class="abs" style="left:0;top:0" width="239" height="134" viewBox="0 0 239 134">
    <rect x="34" y="28" width="80" height="6" rx="1" fill="var(--blue)"/>
    <rect x="144" y="28" width="80" height="6" rx="1" fill="var(--grey-dark)"/>
    <path d="M37 34v76" stroke="var(--blue)" stroke-width=".6"/><path d="M147 34v76" stroke="var(--grey-dark)" stroke-width=".6"/>
    <g fill="var(--blue)"><circle cx="37" cy="55" r="3"/><circle cx="37" cy="81" r="3"/><circle cx="37" cy="108" r="3"/>
      <rect x="53" y="47" width="60" height="16" rx="2"/><rect x="53" y="73" width="60" height="16" rx="2"/><rect x="53" y="100" width="60" height="16" rx="2"/></g>
    <g fill="var(--grey-dark)"><circle cx="147" cy="55" r="3"/><circle cx="147" cy="81" r="3"/><circle cx="147" cy="108" r="3"/>
      <rect x="163" y="47" width="60" height="16" rx="2"/><rect x="163" y="73" width="60" height="16" rx="2"/><rect x="163" y="100" width="60" height="16" rx="2"/></g>
    <g stroke-width=".6"><path d="M40 55h13M40 81h13M40 108h13" stroke="var(--blue)"/><path d="M150 55h13M150 81h13M150 108h13" stroke="var(--grey-dark)"/></g>
    <g font-size="2.4" fill="#fff" text-anchor="middle" font-family="Open Sans, sans-serif" font-weight="700"><text x="74" y="32">LOREM IPSUM</text><text x="184" y="32">LOREM IPSUM</text></g>
  </svg>
  <p class="abs tx w c" style="left:56px;top:51px;width:54px">Lorem ipsum dolor sit amet, consectetur adipiscing elit.</p>
  <p class="abs tx w c" style="left:56px;top:77px;width:54px">Lorem ipsum dolor sit amet, consectetur adipiscing elit.</p>
  <p class="abs tx w c" style="left:56px;top:104px;width:54px">Lorem ipsum dolor sit amet, consectetur adipiscing elit.</p>
  <p class="abs tx w c" style="left:166px;top:51px;width:54px">Lorem ipsum dolor sit amet, consectetur adipiscing elit.</p>
  <p class="abs tx w c" style="left:166px;top:77px;width:54px">Lorem ipsum dolor sit amet, consectetur adipiscing elit.</p>
  <p class="abs tx w c" style="left:166px;top:104px;width:54px">Lorem ipsum dolor sit amet, consectetur adipiscing elit.</p>
</section>

<!-- Row 5 -->
<section class="slide table-slide" style="left:78px;top:701px">
  <div class="hd">EDIT TITLE HERE</div>
  <table class="abs" style="left:17px;top:42px;width:206px;border-collapse:collapse;font-size:3px;font-weight:600;color:var(--grey-dark)">
    <tr style="background:var(--blue);color:#fff;height:9px"><td style="padding-left:18px">Lorem</td><td style="padding-left:18px">Lorem</td><td style="padding-left:18px">Lorem</td><td style="padding-left:18px">Lorem</td></tr>
    <tr style="background:#dcdde3;height:11.5px"><td style="padding-left:18px">Lorem</td><td style="padding-left:18px">Lorem</td><td style="padding-left:18px">Lorem</td><td style="padding-left:18px">Lorem</td></tr>
    <tr style="background:#eeeef1;height:11.5px"><td style="padding-left:18px">Lorem</td><td style="padding-left:18px">Lorem</td><td style="padding-left:18px">Lorem</td><td style="padding-left:18px">Lorem</td></tr>
    <tr style="background:#dcdde3;height:11.5px"><td style="padding-left:18px">Lorem</td><td style="padding-left:18px">Lorem</td><td style="padding-left:18px">Lorem</td><td style="padding-left:18px">Lorem</td></tr>
    <tr style="background:#eeeef1;height:11.5px"><td style="padding-left:18px">Lorem</td><td style="padding-left:18px">Lorem</td><td style="padding-left:18px">Lorem</td><td style="padding-left:18px">Lorem</td></tr>
    <tr style="background:#dcdde3;height:11.5px"><td style="padding-left:18px">Lorem</td><td style="padding-left:18px">Lorem</td><td style="padding-left:18px">Lorem</td><td style="padding-left:18px">Lorem</td></tr>
  </table>
</section>

<section class="slide section-photo-slide" style="left:340px;top:701px">
  <div class="photo" style="left:0;top:0;width:239px;height:134px;background:linear-gradient(90deg,#3a6fb3,#6f98c6 55%,#9bb5d2)" role="img" aria-label="Business people shaking hands against a network globe backdrop"></div>
  <div class="abs" style="left:32px;top:0;width:78px;height:134px;background:rgba(58,114,184,.85)"></div>
  <div class="abs" style="left:38px;top:38px;width:66px;color:#fff;text-align:center">
    <div style="font-size:7.5px;font-weight:600">Section Title</div>
    <p class="tx w c" style="margin-top:4px;font-size:3px;line-height:4px">Lorem ipsum dolor sit amet, consectetur adipiscing elit. Curabitur odio ligula, ultrices eu convallis et ullamcorper libero.</p>
  </div>
</section>

<section class="slide phone-slide" style="left:598px;top:701px">
  <div class="hd">EDIT TITLE HERE</div>
  <svg class="abs" style="left:100px;top:34px" width="38" height="70" viewBox="0 0 38 70">
    <rect x="1" y="1" width="36" height="68" rx="5" fill="var(--blue)"/>
    <rect x="4" y="8" width="30" height="50" fill="#fff"/>
    <circle cx="19" cy="63" r="2.5" fill="#fff"/>
    <text x="19" y="35" font-size="4.5" font-weight="700" fill="var(--blue)" text-anchor="middle" font-family="Open Sans, sans-serif">Brightal</text>
  </svg>
  <div class="row-stack" style="left:30px;top:32px;width:64px">
    <div style="height:18px"><div class="lbl r">Lorem ipsum dolor sit</div><p class="tx" style="text-align:right">Lorem ipsum dolor sit amet, consectetur elit.</p></div>
    <div style="height:18px"><div class="lbl r">Lorem ipsum dolor sit</div><p class="tx" style="text-align:right">Lorem ipsum dolor sit amet, consectetur elit.</p></div>
    <div style="height:18px"><div class="lbl r">Lorem ipsum dolor sit</div><p class="tx" style="text-align:right">Lorem ipsum dolor sit amet, consectetur elit.</p></div>
    <div style="height:18px"><div class="lbl r">Lorem ipsum dolor sit</div><p class="tx" style="text-align:right">Lorem ipsum dolor sit amet, consectetur elit.</p></div>
  </div>
  <div class="row-stack" style="left:150px;top:32px;width:64px">
    <div style="height:18px"><div class="lbl l">Lorem ipsum dolor sit</div><p class="tx">Lorem ipsum dolor sit amet, consectetur elit.</p></div>
    <div style="height:18px"><div class="lbl l">Lorem ipsum dolor sit</div><p class="tx">Lorem ipsum dolor sit amet, consectetur elit.</p></div>
    <div style="height:18px"><div class="lbl l">Lorem ipsum dolor sit</div><p class="tx">Lorem ipsum dolor sit amet, consectetur elit.</p></div>
    <div style="height:18px"><div class="lbl l">Lorem ipsum dolor sit</div><p class="tx">Lorem ipsum dolor sit amet, consectetur elit.</p></div>
  </div>
</section>

<section class="slide gallery-slide" style="left:856px;top:701px">
  <div class="hd">EDIT TITLE HERE</div>
  <div class="abs" style="left:0;top:22px;width:239px;height:105px;background:#ececec"></div>
  <div class="abs" style="left:20px;top:30px;width:200px;display:grid;grid-template-columns:repeat(3,1fr);column-gap:12px;row-gap:8px">
    <div style="background:#fff;padding:2px;height:42px;display:flex;flex-direction:column"><div class="photo" style="position:relative;flex:1" role="img" aria-label="Team meeting photo"></div><div style="background:var(--blue);color:#fff;font-size:2.4px;font-weight:700;text-align:center;padding:1.3px 0">LOREM IPSUM DOLOR</div></div>
    <div style="background:#fff;padding:2px;height:42px;display:flex;flex-direction:column"><div class="photo warm" style="position:relative;flex:1" role="img" aria-label="Colleagues at a desk"></div><div style="background:var(--blue);color:#fff;font-size:2.4px;font-weight:700;text-align:center;padding:1.3px 0">LOREM IPSUM DOLOR</div></div>
    <div style="background:#fff;padding:2px;height:42px;display:flex;flex-direction:column"><div class="photo" style="position:relative;flex:1" role="img" aria-label="Boardroom discussion"></div><div style="background:var(--blue);color:#fff;font-size:2.4px;font-weight:700;text-align:center;padding:1.3px 0">LOREM IPSUM DOLOR</div></div>
    <div style="background:#fff;padding:2px;height:42px;display:flex;flex-direction:column"><div class="photo" style="position:relative;flex:1" role="img" aria-label="Analyst at a computer"></div><div style="background:var(--blue);color:#fff;font-size:2.4px;font-weight:700;text-align:center;padding:1.3px 0">LOREM IPSUM DOLOR</div></div>
    <div style="background:#fff;padding:2px;height:42px;display:flex;flex-direction:column"><div class="photo warm" style="position:relative;flex:1" role="img" aria-label="Group workshop"></div><div style="background:var(--blue);color:#fff;font-size:2.4px;font-weight:700;text-align:center;padding:1.3px 0">LOREM IPSUM DOLOR</div></div>
    <div style="background:#fff;padding:2px;height:42px;display:flex;flex-direction:column"><div class="photo" style="position:relative;flex:1" role="img" aria-label="Presentation in a conference room"></div><div style="background:var(--blue);color:#fff;font-size:2.4px;font-weight:700;text-align:center;padding:1.3px 0">LOREM IPSUM DOLOR</div></div>
  </div>
</section>

<!-- Row 6 -->
<section class="slide map-slide" style="left:78px;top:855px">
  <div class="hd">EDIT TITLE HERE</div>
  <div class="abs" style="left:22px;top:26px;width:194px;height:95px;background:radial-gradient(ellipse at 50% 45%,#b5b5b5 0%,#9a9a9a 55%,rgba(154,154,154,0) 72%)" role="img" aria-label="Grey world map"></div>
  <svg class="abs" style="left:0;top:0" width="239" height="134" viewBox="0 0 239 134">
    <g><path d="M72 46a5 5 0 1 1 10 0c0 4-5 8-5 8s-5-4-5-8z" fill="#222"/><path d="M128 46a5 5 0 1 1 10 0c0 4-5 8-5 8s-5-4-5-8z" fill="#222"/>
    <path d="M137 67a5 5 0 1 1 10 0c0 4-5 8-5 8s-5-4-5-8z" fill="#222"/>
    <path d="M93 76a5 5 0 1 1 10 0c0 4-5 8-5 8s-5-4-5-8z" fill="var(--blue)"/><path d="M175 47a5 5 0 1 1 10 0c0 4-5 8-5 8s-5-4-5-8z" fill="var(--blue)"/>
    <path d="M197 81a5 5 0 1 1 10 0c0 4-5 8-5 8s-5-4-5-8z" fill="var(--blue)"/></g>
    <g fill="#fff"><circle cx="77" cy="46" r="2.6"/><circle cx="133" cy="46" r="2.6"/><circle cx="142" cy="67" r="2.6"/><circle cx="98" cy="76" r="2.6"/><circle cx="180" cy="47" r="2.6"/><circle cx="202" cy="81" r="2.6"/></g>
    <circle cx="17" cy="94" r="3" fill="#222"/><circle cx="17" cy="108" r="3" fill="var(--blue)"/>
    <g font-size="2.8" fill="var(--ink)" font-weight="700" font-family="Open Sans, sans-serif"><text x="24" y="95">EDIT TITLE HERE</text><text x="24" y="109">EDIT TITLE HERE</text></g>
  </svg>
</section>

<section class="slide org-chart-slide" style="left:340px;top:855px">
  <div class="hd">EDIT TITLE HERE</div>
  <svg class="abs" style="left:0;top:0" width="239" height="134" viewBox="0 0 239 134">
    <g fill="none" stroke="#999" stroke-width=".5">
      <path d="M120 35v8M48 43h144M48 43v2M192 43v2M95 43v2M145 43v2"/>
      <path d="M95 50v6h-9v18h9M95 56v4M145 50v6h9v18h-9M145 56v4"/>
      <path d="M48 50v20h38M192 50v20h-38"/>
    </g>
    <g font-size="2.4" fill="#fff" text-anchor="middle" font-family="Open Sans, sans-serif" font-weight="600">
      <rect x="106" y="28" width="28" height="7" fill="var(--grey-dark)"/><text x="120" y="32.6">Title Goes Here</text>
      <rect x="34" y="45" width="28" height="5" fill="var(--grey)"/><text x="48" y="48.6">Title Goes Here</text>
      <rect x="81" y="45" width="28" height="5" fill="var(--blue)"/><text x="95" y="48.6">Title Goes Here</text>
      <rect x="131" y="45" width="28" height="5" fill="var(--blue)"/><text x="145" y="48.6">Title Goes Here</text>
      <rect x="178" y="45" width="28" height="5" fill="var(--grey)"/><text x="192" y="48.6">Title Goes Here</text>
      <rect x="81" y="60" width="28" height="5" fill="var(--blue)"/><text x="95" y="63.6">Title Goes Here</text>
      <rect x="131" y="60" width="28" height="5" fill="var(--blue)"/><text x="145" y="63.6">Title Goes Here</text>
      <rect x="81" y="72" width="28" height="5" fill="var(--blue)"/><text x="95" y="75.6">Title Goes Here</text>
      <rect x="131" y="72" width="28" height="5" fill="var(--blue)"/><text x="145" y="75.6">Title Goes Here</text>
    </g>
  </svg>
  <p class="abs tx c" style="left:25px;top:102px;width:190px">Lorem ipsum dolor sit amet, consectetur adipiscing elit, sed do eiusmod tempor incididunt ut labore. Lorem ipsum dolor sit amet, consectetur adipiscing elit, sed do eiusmod tempor incididunt ut labore. Lorem ipsum dolor sit amet, consectetur adipiscing elit, sed do eiusmod tempor incididunt ut labore.</p>
</section>

<section class="slide icon-list-photo-slide" style="left:598px;top:855px">
  <div class="hd">EDIT TITLE HERE</div>
  <svg class="abs" style="left:0;top:0" width="239" height="134" viewBox="0 0 239 134">
    <g fill="var(--blue)"><circle cx="29" cy="37" r="6.5"/><circle cx="29" cy="60" r="6.5"/><circle cx="29" cy="83" r="6.5"/><circle cx="29" cy="106" r="6.5"/></g>
    <g fill="#fff"><path d="M25 35l4-2l4 2zM25.5 36h7v4h-7z"/><circle cx="27.5" cy="59" r="1.6"/><circle cx="30.5" cy="59" r="1.6"/><path d="M26 62h6v1.5h-6z"/><path d="M25 84l1-3h6l1 3v2h-8z"/><path d="M25 104h8v5h-8zM27.5 102.5h3v1.5h-3z"/></g>
  </svg>
  <div class="row-stack tight" style="left:40px;top:30px;width:68px">
    <div><div class="lbl l" style="color:var(--ink)">Lorem ipsum dolor</div><p class="tx">Lorem ipsum dolor sit amet, consectetur elit.</p></div>
    <div><div class="lbl l" style="color:var(--ink)">Lorem ipsum dolor</div><p class="tx">Lorem ipsum dolor sit amet, consectetur elit.</p></div>
    <div><div class="lbl l" style="color:var(--ink)">Lorem ipsum dolor</div><p class="tx">Lorem ipsum dolor sit amet, consectetur elit.</p></div>
    <div><div class="lbl l" style="color:var(--ink)">Lorem ipsum dolor</div><p class="tx">Lorem ipsum dolor sit amet, consectetur elit.</p></div>
  </div>
  <div class="photo" style="left:128px;top:0;width:111px;height:134px;background:linear-gradient(135deg,#e4e8ee,#a9b6c6 55%,#6b7f97)" role="img" aria-label="Two businessmen in conversation"></div>
</section>

<section class="slide photo-panel-slide" style="left:856px;top:855px">
  <div class="hd">EDIT TITLE HERE</div>
  <div class="photo warm" style="left:0;top:26px;width:120px;height:87px" role="img" aria-label="Colleagues collaborating at a laptop"></div>
  <div class="abs" style="left:120px;top:26px;width:119px;height:87px;background:var(--blue)"></div>
  <svg class="abs" style="left:0;top:0" width="239" height="134" viewBox="0 0 239 134" fill="#fff">
    <path d="M131 40a4 4 0 0 1 7-2a3 3 0 0 1 3 5h-10a2.5 2.5 0 0 1 0-3z"/>
    <circle cx="136" cy="67" r="5" fill="none" stroke="#fff" stroke-width="1.2"/>
    <path d="M131 92l5-2.5l5 2.5zM131.5 93h9v1h-9zM132 94.5h1v4h-1zM135.5 94.5h1v4h-1zM139 94.5h1v4h-1zM131 99h10v1h-10z"/>
  </svg>
  <div class="abs" style="left:148px;top:33px;width:82px">
    <div style="color:#fff;font-size:2.8px;font-weight:700">LOREM IPSUM</div><p class="tx w">Lorem ipsum dolor sit amet, consectetur adipiscing elit, sed do eiusmod tempor incididunt ut labore.</p>
    <div style="color:#fff;font-size:2.8px;font-weight:700;margin-top:11px">LOREM IPSUM</div><p class="tx w">Lorem ipsum dolor sit amet, consectetur adipiscing elit, sed do eiusmod tempor incididunt ut labore.</p>
    <div style="color:#fff;font-size:2.8px;font-weight:700;margin-top:11px">LOREM IPSUM</div><p class="tx w">Lorem ipsum dolor sit amet, consectetur adipiscing elit, sed do eiusmod tempor incididunt ut labore.</p>
  </div>
</section>

<!-- Row 7 -->
<section class="slide quote-slide" style="left:340px;top:1011px">
  <div class="abs" style="left:0;top:0;width:239px;height:67px;background:var(--blue)"></div>
  <div class="abs" style="left:0;top:67px;width:239px;height:67px;background:#e8e8e8"></div>
  <div class="abs" style="left:11px;top:4px;color:#fff;font-size:12px;font-weight:700">&ldquo;</div>
  <div class="abs" style="right:9px;top:44px;color:#fff;font-size:12px;font-weight:700">&rdquo;</div>
  <blockquote class="abs" style="left:26px;top:19px;width:188px;color:#fff;font-size:4.3px;line-height:6px;font-weight:600;text-align:center">&ldquo;Lorem ipsum dolor sit amet, consectetur adipiscing elit. Phasellus sodales, ligula ultrices tempus tristique, tellus justo aliquam dui, nec Lorem ipsum dolor sit amet, consectetur adipiscing elit. elit. Lorem ipsum dolor sit amet, consectetur sit amet, consectetur adipiscing&rdquo;</blockquote>
  <div class="photo grey" style="left:102px;top:66px;width:35px;height:35px;border-radius:50%;border:2px solid #fff" role="img" aria-label="Portrait of the quoted executive"></div>
  <div class="abs" style="left:0;top:106px;width:239px;text-align:center;font-size:5px;font-weight:600;color:var(--ink)">Selina Hartmann</div>
  <div class="abs" style="left:0;top:114px;width:239px;text-align:center;font-size:2.8px;color:var(--muted)">Chief Operating Officer, Aldon Group</div>
</section>

<section class="slide thank-you-slide" style="left:598px;top:1011px">
  <div class="photo warm" style="left:0;top:0;width:239px;height:134px" role="img" aria-label="Happy group of colleagues with a speech bubble"></div>
  <div class="abs" style="left:0;top:0;width:120px;height:134px;background:rgba(58,114,184,.82)"></div>
  <div class="abs" style="left:178px;top:30px;width:40px;height:26px;background:#f2e14c;border-radius:6px"></div>
  <div class="abs" style="left:44px;top:64px;color:#fff;font-size:9px;font-weight:400">THANK YOU</div>
</section>

</body>
</html>
```